Urine collection cup with and without sterile seal sticker

Hello. We need a urine cup label designed please with

Name:
Date of Birth:
Date:
Time:
Temp℃:
Specimen ID:

Product code: TUB-47
Volume markings (e.g., 30 mL, 60 mL, 90 mL).
Vela Drug Tests logo

Could you please provide one version with the additional sterile sticker extending to the top, and one version without the additional sterile sticker?

```html
<!DOCTYPE html>
<html lang="en">
<head>
<meta charset="utf-8">
<title>Vela Drug Tests – Specimen Cup Labels</title>
<link rel="stylesheet" href="https://fonts.googleapis.com/css2?family=Figtree:wght@500;700;800&display=swap">
<style>
  :root {
    --navy: #0f2038;
    --brand-blue: #2a9fe6;
    --scale-blue: #d5eefb;
    --paper: #ffffff;
    --ink: #12233a;
    --bg: #ffffff;
  }
  * { box-sizing: border-box; margin: 0; padding: 0; }
  html, body { width: 1200px; height: 1170px; overflow: hidden; background: var(--bg); }
  body { position: relative; font-family: "Figtree", Arial, sans-serif; color: var(--ink); }

  .label-unit { position: absolute; transform-origin: top left; }
  .label-unit--sealed { width: 451px; height: 493px; }
  .label-unit--plain { width: 379px; height: 329px; }

  .specimen-label {
    position: absolute; left: 0; bottom: 0;
    width: 379px; height: 330px;
    background: var(--paper);
    border: 2px solid var(--navy);
    border-radius: 12px;
    overflow: hidden;
  }
  .label-unit--sealed .specimen-label { border-right: none; border-radius: 12px 0 0 12px; }

  .volume-scale {
    position: absolute; top: 0; bottom: 0; left: 294px; right: 0;
    background: var(--scale-blue);
  }
  .volume-mark {
    position: absolute; left: 10px;
    font-size: 14px; font-weight: 500; line-height: 1;
  }
  .volume-mark--minor { width: 16px; height: 1.5px; background: var(--ink); left: 10px; }

  .brand {
    position: absolute; left: 19px; top: 24px;
    display: flex; align-items: center; gap: 7px;
  }
  .brand-dot { width: 38px; height: 38px; border-radius: 50%; background: var(--brand-blue); }
  .brand-name { font-size: 29px; font-weight: 800; color: var(--navy); letter-spacing: -0.3px; }

  .record-fields { position: absolute; left: 19px; top: 87px; width: 261px; }
  .record-field {
    display: flex; align-items: flex-end;
    height: 31.5px; font-size: 16.5px; font-weight: 500;
  }
  .record-field .entry-line { flex: 1; border-bottom: 1.3px solid var(--ink); margin: 0 0 6px 8px; }
  .record-field--tight .entry-line { margin-left: 1px; }
  .record-field sup { font-size: 10px; font-weight: 700; }

  .product-code {
    position: absolute; left: 18px; top: 291px;
    font-size: 20.5px; font-weight: 700;
  }

  .seal-sticker {
    position: absolute; left: 366px; top: 0;
    width: 85px; height: 493px;
    background: var(--navy);
    border-radius: 14px;
  }
  .seal-dot {
    position: absolute; left: 24px; top: 19px;
    width: 38px; height: 38px; border-radius: 50%; background: var(--brand-blue);
  }
  .seal-title {
    position: absolute; left: 22px; top: 168px;
    writing-mode: vertical-rl;
    color: var(--paper); font-size: 40px; font-weight: 700; line-height: 1;
  }
  .seal-note {
    position: absolute; left: 26px; top: 309px;
    writing-mode: vertical-rl;
    color: var(--paper); font-size: 12.5px; font-weight: 500; line-height: 1.3;
    text-transform: uppercase;
  }
</style>
</head>
<body>

  <!-- Small sealed version -->
  <div class="label-unit label-unit--sealed" style="left:146px; top:168px; transform:scale(0.69);">
    <div class="specimen-label">
      <div class="volume-scale">
        <span class="volume-mark" style="top:86px">–&nbsp; 90 mL</span>
        <span class="volume-mark volume-mark--minor" style="top:135px"></span>
        <span class="volume-mark" style="top:170px">–&nbsp; 60 mL</span>
        <span class="volume-mark volume-mark--minor" style="top:218px"></span>
        <span class="volume-mark" style="top:252px">–&nbsp; 30 mL</span>
      </div>
      <div class="brand"><span class="brand-dot"></span><span class="brand-name">Vela Drug Tests</span></div>
      <div class="record-fields">
        <div class="record-field">Name:<span class="entry-line"></span></div>
        <div class="record-field record-field--tight">Date of Birth:<span class="entry-line"></span></div>
        <div class="record-field">Date:<span class="entry-line"></span></div>
        <div class="record-field">Time:<span class="entry-line"></span></div>
        <div class="record-field">Temp<sup>o</sup>C:<span class="entry-line"></span></div>
        <div class="record-field record-field--tight">Specimen ID:<span class="entry-line"></span></div>
      </div>
      <div class="product-code">Product code: TUB-47</div>
    </div>
    <div class="seal-sticker">
      <span class="seal-dot"></span>
      <span class="seal-title">Sterile</span>
      <span class="seal-note">Interior long as seal<br>remains intact</span>
    </div>
  </div>

  <!-- Large sealed version -->
  <div class="label-unit label-unit--sealed" style="left:583px; top:66px;">
    <div class="specimen-label">
      <div class="volume-scale">
        <span class="volume-mark" style="top:86px">–&nbsp; 90 mL</span>
        <span class="volume-mark volume-mark--minor" style="top:135px"></span>
        <span class="volume-mark" style="top:170px">–&nbsp; 60 mL</span>
        <span class="volume-mark volume-mark--minor" style="top:218px"></span>
        <span class="volume-mark" style="top:252px">–&nbsp; 30 mL</span>
      </div>
      <div class="brand"><span class="brand-dot"></span><span class="brand-name">Vela Drug Tests</span></div>
      <div class="record-fields">
        <div class="record-field">Name:<span class="entry-line"></span></div>
        <div class="record-field record-field--tight">Date of Birth:<span class="entry-line"></span></div>
        <div class="record-field">Date:<span class="entry-line"></span></div>
        <div class="record-field">Time:<span class="entry-line"></span></div>
        <div class="record-field">Temp<sup>o</sup>C:<span class="entry-line"></span></div>
        <div class="record-field record-field--tight">Specimen ID:<span class="entry-line"></span></div>
      </div>
      <div class="product-code">Product code: TUB-47</div>
    </div>
    <div class="seal-sticker">
      <span class="seal-dot"></span>
      <span class="seal-title">Sterile</span>
      <span class="seal-note">Interior long as seal<br>remains intact</span>
    </div>
  </div>

  <!-- Small version without seal -->
  <div class="label-unit label-unit--plain" style="left:161px; top:802px; transform:scale(0.71);">
    <div class="specimen-label">
      <div class="volume-scale">
        <span class="volume-mark" style="top:86px">–&nbsp; 90 mL</span>
        <span class="volume-mark volume-mark--minor" style="top:135px"></span>
        <span class="volume-mark" style="top:170px">–&nbsp; 60 mL</span>
        <span class="volume-mark volume-mark--minor" style="top:218px"></span>
        <span class="volume-mark" style="top:252px">–&nbsp; 30 mL</span>
      </div>
      <div class="brand"><span class="brand-dot"></span><span class="brand-name">Vela Drug Tests</span></div>
      <div class="record-fields">
        <div class="record-field">Name:<span class="entry-line"></span></div>
        <div class="record-field record-field--tight">Date of Birth:<span class="entry-line"></span></div>
        <div class="record-field">Date:<span class="entry-line"></span></div>
        <div class="record-field">Time:<span class="entry-line"></span></div>
        <div class="record-field">Temp<sup>o</sup>C:<span class="entry-line"></span></div>
        <div class="record-field record-field--tight">Specimen ID:<span class="entry-line"></span></div>
      </div>
      <div class="product-code">Product code: TUB-47</div>
    </div>
  </div>

  <!-- Large version without seal -->
  <div class="label-unit label-unit--plain" style="left:583px; top:724px;">
    <div class="specimen-label">
      <div class="volume-scale">
        <span class="volume-mark" style="top:86px">–&nbsp; 90 mL</span>
        <span class="volume-mark volume-mark--minor" style="top:135px"></span>
        <span class="volume-mark" style="top:170px">–&nbsp; 60 mL</span>
        <span class="volume-mark volume-mark--minor" style="top:218px"></span>
        <span class="volume-mark" style="top:252px">–&nbsp; 30 mL</span>
      </div>
      <div class="brand"><span class="brand-dot"></span><span class="brand-name">Vela Drug Tests</span></div>
      <div class="record-fields">
        <div class="record-field">Name:<span class="entry-line"></span></div>
        <div class="record-field record-field--tight">Date of Birth:<span class="entry-line"></span></div>
        <div class="record-field">Date:<span class="entry-line"></span></div>
        <div class="record-field">Time:<span class="entry-line"></span></div>
        <div class="record-field">Temp<sup>o</sup>C:<span class="entry-line"></span></div>
        <div class="record-field record-field--tight">Specimen ID:<span class="entry-line"></span></div>
      </div>
      <div class="product-code">Product code: TUB-47</div>
    </div>
  </div>

</body>
</html>
```